Offshore Energy Projects Management Consultancy needs a business card design

Logo available. We provide teams to deliver engineering consultancy, project management and delivery teams mainly in the offshore renewables sector. The company is all about bringing the right people to a project to deliver the scope.

The business card will be used for all staff.

The business card should be quite simple, vibrant and uncluttered but convey experience, enthusiasm and integration.

Target Market(s)

Energy Project Developers and Tier 1 construction companies

Contact Information for Business Card

Logo should be on the back of the card. I'm happy for the designer to play with the colour of the logo and background colour.

Front of the card should convey all the must have information in a clear and professional manner but without being overly traditional.

Colors

Designer to choose colors to be used in the design.

Requirements
Must have
• Land Line Tel Number, Mobile Tel Number, Email, business address, web address.

```html
<!DOCTYPE html>
<html lang="en">
<head>
<meta charset="utf-8">
<title>Seaward Delivery Group – Business Card</title>
<link rel="stylesheet" href="https://fonts.googleapis.com/css2?family=Lato:wght@400;700&display=swap">
<style>
  :root {
    --stage: #2b2b2b;
    --card: #1c1c1d;
    --card-edge: #262628;
    --brand-blue: #1f86d6;
    --brand-grey: #77787a;
    --text-light: #d9d9d9;
    --text-muted: #a9a9a9;
  }
  * { box-sizing: border-box; margin: 0; padding: 0; }
  html, body { width: 1200px; height: 997px; overflow: hidden; }
  body {
    background: var(--stage);
    font-family: "Lato", Arial, sans-serif;
    position: relative;
  }
  .card {
    position: absolute;
    width: 760px;
    height: 430px;
    background: var(--card);
    border: 1px solid var(--card-edge);
    border-radius: 34px;
    box-shadow: 0 18px 40px rgba(0,0,0,0.45);
  }
  .card--back { left: 80px; top: 56px; }
  .card--front { left: 360px; top: 510px; }

  /* shared wordmark */
  .brand {
    display: flex;
    align-items: center;
    gap: 16px;
  }
  .brand__dot {
    width: 22px; height: 22px;
    border-radius: 50%;
    background: var(--brand-blue);
    flex: none;
  }
  .brand__name {
    font-weight: 700;
    color: var(--brand-blue);
    letter-spacing: 1px;
    text-transform: uppercase;
  }

  /* back face */
  .card--back .brand {
    position: absolute;
    left: 0; right: 0; top: 170px;
    justify-content: center;
  }
  .card--back .brand__name { font-size: 38px; }
  .back__web {
    position: absolute;
    left: 0; right: 0; bottom: 70px;
    text-align: center;
    color: var(--text-muted);
    font-size: 19px;
    letter-spacing: 1px;
  }

  /* front face */
  .card--front .brand {
    position: absolute;
    left: 56px; top: 168px;
    width: 320px;
  }
  .card--front .brand__name {
    font-size: 26px;
    line-height: 1.2;
    width: 280px;
  }
  .front__divider {
    position: absolute;
    left: 402px; top: 60px;
    width: 2px; height: 300px;
    background: linear-gradient(to bottom, rgba(31,134,214,0), var(--brand-blue) 35%, var(--brand-blue) 65%, rgba(31,134,214,0));
  }
  .contact {
    position: absolute;
    left: 432px; top: 92px;
    width: 300px;
    color: var(--text-light);
    font-size: 16px;
    line-height: 1.45;
  }
  .contact__name { color: var(--brand-blue); font-size: 20px; }
  .contact__role { font-weight: 700; font-size: 14px; margin-bottom: 14px; }
  .contact__address { margin-bottom: 8px; }
  .contact__list { list-style: none; }
  .contact__list li { display: flex; align-items: center; gap: 12px; }
  .contact__list svg { width: 14px; height: 14px; fill: var(--brand-blue); flex: none; }
</style>
</head>
<body>

<section class="card card--back" aria-label="Card back">
  <div class="brand">
    <span class="brand__dot"></span>
    <span class="brand__name">Seaward Delivery Group</span>
  </div>
  <p class="back__web">www.seawarddeliverygroup.com</p>
</section>

<section class="card card--front" aria-label="Card front">
  <div class="brand">
    <span class="brand__dot"></span>
    <span class="brand__name">Seaward Delivery Group</span>
  </div>
  <div class="front__divider"></div>
  <div class="contact">
    <p class="contact__name">Maren Holloway-Quinn</p>
    <p class="contact__role">Registered Psychologist</p>
    <p class="contact__address">2207-48 Ave Box 1184 Harlow,<br>AB T6K 2R3</p>
    <ul class="contact__list">
      <li><svg viewBox="0 0 16 16"><path d="M3 2h3l1.5 3.5-2 1.2a9 9 0 0 0 3.8 3.8l1.2-2L14 10v3a1 1 0 0 1-1 1A11 11 0 0 1 2 3a1 1 0 0 1 1-1z"/></svg>555.204.3817</li>
      <li><svg viewBox="0 0 16 16"><path d="M3 2h3l1.5 3.5-2 1.2a9 9 0 0 0 3.8 3.8l1.2-2L14 10v3a1 1 0 0 1-1 1A11 11 0 0 1 2 3a1 1 0 0 1 1-1z"/></svg>555.204.6691</li>
      <li><svg viewBox="0 0 16 16"><path d="M1 3h14v10H1z M1 3l7 6 7-6" stroke="#1c1c1d" stroke-width="1"/></svg>maren@seawarddelivery.ca</li>
      <li><svg viewBox="0 0 16 16"><circle cx="8" cy="8" r="7"/><path d="M1 8h14M8 1c3 3 3 11 0 14M8 1c-3 3-3 11 0 14" stroke="#1c1c1d" stroke-width="1" fill="none"/></svg>www.seawarddelivery.ca</li>
    </ul>
  </div>
</section>

</body>
</html>
```